Customer Quotes Page

We want to create a fun looking customer quotes page. The point of this project is to be get creative with the treatment of the quotes. Our current version of the page just has them listed in two columns, which is pretty boring. We need something more interesting but it should still fit into our site. Attached is the current Testimonials page as it looks now. The two column layout does not have to be maintained, you can list the manager quotes above the resident quotes. Also not all quotes have to be used, we just need to see 5-10 from the resident and management categories.
The header and footer is already designed, so those elements need to stay the same. The background color also needs to remain same (light fuzzy gray)
Here is a site that we like: https://plumkitehub.example/info/ (take a look at the "What people are saying" section). But this is just an example, we might like something radically different. The point is to be as creative with the quote boxes as possible. A very refined but subdued approach might also be interesting.
FINAL FILE SHOULD BE A PSD FILE WITH LAYERS. WE WILL CODE THE PAGE OURSELVES.
Updates
What we're most interested in this contest is the graphic treatment of the quotes. Right now they're simply gray boxes. We'd like to see what you can do with this. The layout of the page can remain same (two-column) but a 1 column layout is also fine. Also please don't add any additional elements to the page like stock photo. We are only interested in the treatment of the quotes and anything goes whether it is very elegant, cartoony, bold and colorful, hand-drawn, 3D, textured......

```html
<!DOCTYPE html>
<html lang="en">
<head>
<meta charset="utf-8">
<title>TowerDesk – Testimonials</title>
<link href="https://fonts.googleapis.com/css2?family=Arimo:wght@400;700&family=Tinos:ital,wght@0,400;0,700;1,400&display=swap" rel="stylesheet">
<style>
:root{
  --page-bg:#ebebeb;
  --ink:#333333;
  --muted:#777777;
  --brand-red:#b3201c;
  --nav-dark:#2e2e2e;
  --nav-mid:#474747;
  --accent-orange:#e0990d;
  --bubble-dark:#3b3b3b;
  --bubble-light:#fffdf4;
  --footer-bg:#5b5b5b;
  --footer-text:#e6e6e6;
  --white:#ffffff;
}
*{box-sizing:border-box;margin:0;padding:0}
html,body{width:1200px;height:2755px;overflow:hidden}
body{background:var(--page-bg);font-family:"Arimo",Arial,sans-serif;color:var(--ink);position:relative}
.wrap{width:906px;margin:0 auto;position:relative}

/* utility bar */
.utility-bar{height:25px;background:#d9d9d9;border-bottom:1px solid #c4c4c4}
.utility-bar .wrap{display:flex;align-items:stretch;height:25px}
.site-tab{font-size:13px;padding:5px 14px 0;color:#555;text-decoration:underline}
.site-tab.is-active{background:var(--white);color:var(--brand-red);border-top:3px solid var(--brand-red);padding-top:3px}
.login-btn{margin-left:auto;background:var(--nav-dark);color:var(--white);font-size:11px;font-weight:700;padding:6px 20px 0;letter-spacing:.5px}

/* header */
.masthead{height:150px}
.masthead .wrap{height:150px}
.brand{position:absolute;left:0;top:94px;display:flex;align-items:center;gap:10px;font-family:"Arimo",Arial,sans-serif;font-weight:700;font-size:40px;color:var(--ink);letter-spacing:-1px}
.brand-mark{width:30px;height:30px;background:var(--brand-red)}
.tagline{position:absolute;right:0;top:26px;text-align:right;font-family:"Tinos",Georgia,serif;font-style:italic;color:#8a8a8a;font-size:17px;line-height:1.35}

/* nav */
.main-nav{height:56px;background:linear-gradient(#4d4d4d,var(--nav-dark));}
.main-nav .wrap{display:flex;height:56px}
.nav-item{flex:1;display:flex;align-items:center;justify-content:center;text-align:center;color:var(--white);font-size:14px;line-height:1.2;border-right:1px solid #5c5c5c;position:relative}
.nav-item.is-current{background:linear-gradient(#5a5a5a,#3e3e3e)}
.nav-item.is-current::after{content:"";position:absolute;bottom:-8px;left:50%;margin-left:-8px;border:8px solid transparent;border-bottom:0;border-top-color:#3e3e3e}
.nav-item.demo{background:linear-gradient(#f0aa22,var(--accent-orange));color:#3a2600;font-weight:700;border-right:0}

/* content */
.content{padding-top:17px}
.eyebrow{font-size:15px;letter-spacing:.5px;color:#444}
.section-title{font-family:"Tinos",Georgia,serif;color:var(--brand-red);font-size:46px;font-weight:400;line-height:1;margin-top:8px}
.title-rule{height:5px;background:#555;border-radius:3px;margin:14px 0 26px;opacity:.8}

.quote-row{height:178px;position:relative}
.avatar{position:absolute;top:10px;width:134px;height:134px;border-radius:50%;border:5px solid #444;background:radial-gradient(circle,#ffffff 55%,#e6e6e6)}
.avatar-name{position:absolute;top:149px;width:134px;text-align:center;font-size:12px;color:#555}
.bubble{position:absolute;top:4px;height:132px;border:4px solid var(--white);box-shadow:0 3px 8px rgba(0,0,0,.35);padding:18px 28px 0 20px;font-family:"Tinos",Georgia,serif;font-size:20.5px;line-height:1.42}
.bubble::before{content:"\201C";font-size:42px;line-height:0;position:relative;top:12px;margin-right:6px;font-weight:700}
.bubble .close-mark{font-size:42px;line-height:0;position:relative;top:14px;margin-left:4px;font-weight:700}
.bubble::after{content:"";position:absolute;bottom:-18px;border:14px solid transparent;border-bottom:0}
.quote-date{position:absolute;top:144px;font-size:12px;color:#444}

.quote-row.manager .avatar{left:18px}
.quote-row.manager .avatar-name{left:18px}
.quote-row.manager .bubble{left:207px;right:0;background:var(--bubble-dark);color:var(--white)}
.quote-row.manager .bubble::after{left:40px;border-top-color:var(--bubble-dark)}
.quote-row.manager .quote-date{left:214px}

.quote-row.resident .avatar{right:16px;border-color:var(--accent-orange)}
.quote-row.resident .avatar-name{right:16px;color:var(--accent-orange)}
.quote-row.resident .bubble{left:0;right:186px;background:var(--accent-orange);color:var(--bubble-light)}
.quote-row.resident .bubble::after{right:40px;border-top-color:var(--accent-orange)}
.quote-row.resident .quote-date{right:186px}
.quote-row.resident .connector{position:absolute;right:150px;top:76px;width:36px;height:3px;background:var(--accent-orange)}

.resident-title{margin-top:51px}

.read-more{display:block;margin:34px 0 0;height:32px;border-radius:16px;background:linear-gradient(#f7f7f7,#d7d7d7);border:1px solid #bdbdbd;text-align:center;font-size:13px;line-height:30px;color:#444}

/* footer */
.site-footer{position:absolute;left:0;right:0;top:2366px;bottom:0;background:var(--footer-bg);color:var(--footer-text)}
.footer-cols{display:flex;padding-top:34px}
.footer-col{width:226px;font-family:"Tinos",Georgia,serif;font-size:15px;line-height:1.3}
.footer-col h4{font-family:"Arimo",Arial,sans-serif;font-size:14px;font-weight:700;margin-bottom:30px;color:var(--white)}
.footer-col a{display:block;color:var(--footer-text);text-decoration:underline}
.phone{font-family:"Arimo",Arial,sans-serif;font-size:25px;font-weight:700;color:var(--white)}
.hours{font-size:11px;margin:4px 0 12px}
.small-link{font-size:11px}
.stay-title{font-family:"Arimo",Arial,sans-serif;font-size:14px;font-weight:700;margin:26px 0 10px;color:var(--white)}
.social a{display:flex;align-items:center;gap:8px;font-size:14px}
.social i{width:12px;height:12px;background:#9a9a9a}
.copyright{position:absolute;left:147px;top:340px;font-family:"Tinos",Georgia,serif;font-size:14px;color:var(--footer-text)}
.legal{position:absolute;left:147px;top:362px;font-size:10px;color:#cfcfcf}
</style>
</head>
<body>

<div class="utility-bar">
  <div class="wrap">
    <span class="site-tab is-active">TowerDesk</span>
    <span class="site-tab">GateNote</span>
    <span class="site-tab">Partner Circle</span>
    <span class="site-tab">International</span>
    <span class="login-btn">LOGIN</span>
  </div>
</div>

<header class="masthead">
  <div class="wrap">
    <div class="brand"><span class="brand-mark"></span>TowerDesk.com</div>
    <p class="tagline">The Ultimate Integrated Platform for<br>Residential Property Managers &amp; Their Communities</p>
  </div>
</header>

<nav class="main-nav">
  <div class="wrap">
    <span class="nav-item">Home</span>
    <span class="nav-item">About<br>TowerDesk</span>
    <span class="nav-item">Management<br>Experience</span>
    <span class="nav-item">Resident<br>Experience</span>
    <span class="nav-item">Technology<br>&amp; Innovation</span>
    <span class="nav-item is-current">Testimonial</span>
    <span class="nav-item">Support</span>
    <span class="nav-item demo">Request<br>Demo</span>
  </div>
</nav>

<main class="content">
  <div class="wrap">
    <p class="eyebrow">TESTIMONIALS</p>
    <h1 class="section-title">Manager Quotes</h1>
    <div class="title-rule"></div>

    <div class="quote-row manager">
      <div class="avatar" role="img" aria-label="Manager portrait"></div>
      <span class="avatar-name">Dolor sit amet</span>
      <blockquote class="bubble">Lorem ipsum dolor sit amet, consectetur adipiscing elit. Cras aliquet risus scelerisque nibh facilisis elementum ut ac mi. Donec a consequat leo. Pellentesque ligula nisi, vestibulum sed elementum quis, lacinia id dui.<span class="close-mark">&#8221;</span></blockquote>
      <span class="quote-date">25/05/2011</span>
    </div>
    <div class="quote-row resident">
      <blockquote class="bubble">Lorem ipsum dolor sit amet, consectetur adipiscing elit. Cras aliquet risus scelerisque nibh facilisis elementum ut ac mi. Donec a consequat leo. Pellentesque ligula nisi, vestibulum sed elementum quis, lacinia id dui.<span class="close-mark">&#8221;</span></blockquote>
      <span class="connector"></span>
      <div class="avatar" role="img" aria-label="Manager portrait"></div>
      <span class="avatar-name">Dolor sit amet</span>
      <span class="quote-date">25/05/2011</span>
    </div>
    <div class="quote-row manager">
      <div class="avatar" role="img" aria-label="Manager portrait"></div>
      <span class="avatar-name">Dolor sit amet</span>
      <blockquote class="bubble">Lorem ipsum dolor sit amet, consectetur adipiscing elit. Cras aliquet risus scelerisque nibh facilisis elementum ut ac mi. Donec a consequat leo. Pellentesque ligula nisi, vestibulum sed elementum quis, lacinia id dui.<span class="close-mark">&#8221;</span></blockquote>
      <span class="quote-date">25/05/2011</span>
    </div>
    <div class="quote-row resident">
      <blockquote class="bubble">Lorem ipsum dolor sit amet, consectetur adipiscing elit. Cras aliquet risus scelerisque nibh facilisis elementum ut ac mi. Donec a consequat leo. Pellentesque ligula nisi, vestibulum sed elementum quis, lacinia id dui.<span class="close-mark">&#8221;</span></blockquote>
      <span class="connector"></span>
      <div class="avatar" role="img" aria-label="Manager portrait"></div>
      <span class="avatar-name">Dolor sit amet</span>
      <span class="quote-date">25/05/2011</span>
    </div>
    <div class="quote-row manager">
      <div class="avatar" role="img" aria-label="Manager portrait"></div>
      <span class="avatar-name">Dolor sit amet</span>
      <blockquote class="bubble">Lorem ipsum dolor sit amet, consectetur adipiscing elit. Cras aliquet risus scelerisque nibh facilisis elementum ut ac mi. Donec a consequat leo. Pellentesque ligula nisi, vestibulum sed elementum quis, lacinia id dui.<span class="close-mark">&#8221;</span></blockquote>
      <span class="quote-date">25/05/2011</span>
    </div>

    <h2 class="section-title resident-title">Resident Quotes</h2>
    <div class="title-rule"></div>

    <div class="quote-row resident">
      <blockquote class="bubble">Lorem ipsum dolor sit amet, consectetur adipiscing elit. Cras aliquet risus scelerisque nibh facilisis elementum ut ac mi. Donec a consequat leo. Pellentesque ligula nisi, vestibulum sed elementum quis, lacinia id dui.<span class="close-mark">&#8221;</span></blockquote>
      <span class="connector"></span>
      <div class="avatar" role="img" aria-label="Resident portrait"></div>
      <span class="avatar-name">Dolor sit amet</span>
      <span class="quote-date">25/05/2011</span>
    </div>
    <div class="quote-row manager">
      <div class="avatar" role="img" aria-label="Resident portrait"></div>
      <span class="avatar-name">Dolor sit amet</span>
      <blockquote class="bubble">Lorem ipsum dolor sit amet, consectetur adipiscing elit. Cras aliquet risus scelerisque nibh facilisis elementum ut ac mi. Donec a consequat leo. Pellentesque ligula nisi, vestibulum sed elementum quis, lacinia id dui.<span class="close-mark">&#8221;</span></blockquote>
      <span class="quote-date">25/05/2011</span>
    </div>
    <div class="quote-row resident">
      <blockquote class="bubble">Lorem ipsum dolor sit amet, consectetur adipiscing elit. Cras aliquet risus scelerisque nibh facilisis elementum ut ac mi. Donec a consequat leo. Pellentesque ligula nisi, vestibulum sed elementum quis, lacinia id dui.<span class="close-mark">&#8221;</span></blockquote>
      <span class="connector"></span>
      <div class="avatar" role="img" aria-label="Resident portrait"></div>
      <span class="avatar-name">Dolor sit amet</span>
      <span class="quote-date">25/05/2011</span>
    </div>
    <div class="quote-row manager">
      <div class="avatar" role="img" aria-label="Resident portrait"></div>
      <span class="avatar-name">Dolor sit amet</span>
      <blockquote class="bubble">Lorem ipsum dolor sit amet, consectetur adipiscing elit. Cras aliquet risus scelerisque nibh facilisis elementum ut ac mi. Donec a consequat leo. Pellentesque ligula nisi, vestibulum sed elementum quis, lacinia id dui.<span class="close-mark">&#8221;</span></blockquote>
      <span class="quote-date">25/05/2011</span>
    </div>
    <div class="quote-row resident">
      <blockquote class="bubble">Lorem ipsum dolor sit amet, consectetur adipiscing elit. Cras aliquet risus scelerisque nibh facilisis elementum ut ac mi. Donec a consequat leo. Pellentesque ligula nisi, vestibulum sed elementum quis, lacinia id dui.<span class="close-mark">&#8221;</span></blockquote>
      <span class="connector"></span>
      <div class="avatar" role="img" aria-label="Resident portrait"></div>
      <span class="avatar-name">Dolor sit amet</span>
      <span class="quote-date">25/05/2011</span>
    </div>

    <span class="read-more">Read More</span>
  </div>
</main>

<footer class="site-footer">
  <div class="wrap">
    <div class="footer-cols">
      <div class="footer-col">
        <h4>TowerDesk</h4>
        <a>Home</a><a>About TowerDesk</a><a>Management Experience</a><a>Resident Experience</a><a>Technology &amp; Innovation</a><a>Testimonial</a><a>Support</a><a>Request Demo</a>
      </div>
      <div class="footer-col">
        <h4>GateNote</h4>
        <a>Home</a><a>Why GateNote?</a><a>Features</a><a>Product List</a><a>Installation Updates</a><a>The GateNote Story</a><a>Contact Us</a><a>FAQ</a>
      </div>
      <div class="footer-col">
        <h4>Partner Circle</h4>
        <a>Home</a><a>The Opportunity</a><a>FAQ</a><a>Join Partner Circle</a>
      </div>
      <div class="footer-col">
        <h4>Sales | Support</h4>
        <div class="phone">1(800) 555-0142</div>
        <div class="hours">9:00am - 5:00pm EST</div>
        <a class="small-link">Email Support</a>
        <a class="small-link">Email Sales</a>
        <div class="stay-title">Stay in touch</div>
        <div class="social">
          <a><i></i>Newsletter</a><a><i></i>Blog</a><a><i></i>Chirp</a><a><i></i>Friendbook</a>
        </div>
      </div>
    </div>
  </div>
  <p class="copyright">© Copyright 2000-2011 TowerDesk.com LLC. All rights reserved. 12 Harbor Lane, 4th Floor, Springfield, NY 10001.</p>
  <p class="legal">Privacy Policy | Terms and Conditions | Tell Us What You Think</p>
</footer>

</body>
</html>
```